Flyer-Design für Vermittlung von Büromaschinen
Zielgruppe
Wir vertreiben Büromaschinen hauptsächlich hochwertige Kopierautomaten für Büros, Steuerberater, Rechtsanwälte usw.
Besonderen Augenmerk auf gebrauchte, generalüberholte Maschinen zur Miete an den Kunden, damit die Rohstoffe möglichst lange genutzt werden um die Umwelt zu schonen. zum Beispiel:
Willkommen in der Wegwerfgesellschaft.
Früher oder später wird alles weggeworfen. In der Konsumgesellschaft wandern aber auch gebrauchsfertige und neuwertige Produkte auf den Müll. Dieses hat fatale Konsequenzen: Klimawandel, Artensterben, Wassermangel- schon heute für viele existenzbedrohend. So wie wir wirtschaften, kann es nicht weitergehen! Wir müssen Rohstoffe möglichst lange nutzen, um dadurch die Umwelt zu schonen, denn wenn wir so weitermachen wie bisher werden 2050 mehr Plastik in unseren Ozeanen schwimmen als Fische. Helfen Sie uns beim Aufbau einer erfolgreichen Nutzungsform, bei der funktionstüchtige Kopierautomaten weiterhin eingesetzt werden sodass sichergestellt wird das Rohstoffe möglichst lange genutzt werden, um dadurch die Umwelt zu schonen. Bitte beachten Sie unser beigefügtes Angebot damit die Nachhaltigkeit gewinnt.
Wir kaufen gebrauchte Kopierautomaten von Leasinggesellschaften und bereiten diese in unserer Werkstatt auf. Diese dann neuwertigen, funktionstüchtigen Maschinen sollen dann vermietet werden.
Aufgabenstellung
Wir benötigen einen Flyer und ein entsprechendes Anschreiben.
Bilder und Texte können von der Website entnommen werden:
https://www.brettel-bueroservice.de/
Bei Anfrage kann ich Ihnen auch gerne die Bilder zur Verfügung stellen.
Bezüglich der Texte, würde ich mich auch über Vorschläge von Ihrer Seite freuen.

```html
<!DOCTYPE html>
<html lang="de">
<head>
<meta charset="utf-8">
<title>brettel Büroservice – Flyer</title>
<link rel="stylesheet" href="https://fonts.googleapis.com/css2?family=Titillium+Web:ital,wght@1,900&family=Roboto+Condensed:wght@300;400&family=Didact+Gothic&family=Oswald:wght@300&family=Ubuntu:wght@400&display=swap">
<style>
  :root{
    --teal:#6cc4bf;
    --teal-dark:#0e7a6e;
    --ink:#4a4a4a;
    --navy:#232a66;
    --paper:#ffffff;
    --stage:#8a8a8a;
  }
  *{box-sizing:border-box;margin:0;padding:0}
  html,body{width:1200px;height:552px;overflow:hidden;background:var(--stage)}
  .canvas{position:relative;width:1200px;height:552px}
  .flyer{position:absolute;top:51px;width:450px;height:450px;background:var(--paper);overflow:hidden;box-shadow:0 6px 18px rgba(0,0,0,.35)}
  .flyer--front{left:75px}
  .flyer--back{left:675px}

  /* front */
  .hero-photo{position:absolute;left:0;top:0;width:260px;height:414px;
    background:linear-gradient(150deg,#3c444c 0%,#d9dcdf 35%,#eef0f1 55%,#3a4149 80%,#2b3137 100%);
    clip-path:polygon(0 0,225px 0,260px 414px,0 414px)}
  .claim{position:absolute;right:0;background:var(--teal);color:#fff;
    font-family:"Titillium Web",sans-serif;font-weight:900;font-style:italic;
    text-transform:uppercase;letter-spacing:.5px;line-height:1.08;white-space:nowrap}
  .claim--help{top:34px;width:222px;padding:10px 10px 10px 16px;font-size:16.5px}
  .claim--planet{top:150px;width:202px;padding:9px 8px 9px 14px;font-size:16.5px}
  .brand{position:absolute;left:250px;top:364px;font-family:"Ubuntu",sans-serif;
    font-size:22px;color:var(--navy);white-space:nowrap}
  .band{position:absolute;left:0;bottom:0;width:100%;height:34px;background:var(--teal);color:#fff;
    font-family:"Oswald",sans-serif;font-weight:300;font-size:15px;letter-spacing:1.6px;
    display:flex;align-items:center;justify-content:center;white-space:nowrap}

  /* back */
  .headline{position:absolute;left:35px;top:10px;font-family:"Roboto Condensed",sans-serif;
    font-weight:400;font-size:16.5px;color:var(--teal);white-space:nowrap}
  .headline--sub{top:308px}
  .copy{position:absolute;width:171px;font-family:"Didact Gothic",sans-serif;font-size:8.6px;
    line-height:12.8px;color:var(--ink);letter-spacing:.2px}
  .copy span{display:block;white-space:nowrap;text-align:justify;text-align-last:justify}
  .copy span.end{text-align-last:left}
  .copy--intro-a{left:35px;top:30px}
  .copy--intro-b{left:229px;top:30px}
  .copy--join-a{left:35px;top:332px}
  .copy--join-b{left:229px;top:319px}

  .cycle{position:absolute;left:0;top:0}
  .device{position:absolute;border-radius:3px}
  .device--copier{left:124px;top:112px;width:117px;height:121px;
    background:linear-gradient(90deg,#2f3338 0%,#4a4f55 55%,#e9eaec 72%,#c9cbce 100%)}
  .device--printer{left:284px;top:160px;width:76px;height:70px;
    background:linear-gradient(180deg,#e6e7e9,#b9bbbe)}
  .step{position:absolute;font-family:"Didact Gothic",sans-serif;font-size:9px;line-height:13px;
    color:var(--ink);text-align:center;letter-spacing:.4px;white-space:nowrap}
  .step--1{left:44px;top:168px;width:80px}
  .step--2{left:262px;top:101px;width:72px}
  .step--3{left:302px;top:235px;width:98px}
  .step-no{position:absolute;font-family:"Roboto Condensed",sans-serif;font-weight:300;font-size:23px;
    line-height:1;color:var(--ink)}
  .step-no--1{left:32px;top:186px}
  .step-no--2{left:246px;top:103px}
  .step-no--3{left:404px;top:237px}
  .together{position:absolute;left:134px;top:252px;width:128px;text-align:center;
    font-family:"Titillium Web",sans-serif;font-weight:900;font-style:italic;font-size:12px;
    line-height:14.5px;color:var(--teal);letter-spacing:1px;text-transform:uppercase;white-space:nowrap}
  .contact{position:absolute;left:33px;top:386px;width:377px;font-family:"Didact Gothic",sans-serif;
    font-size:9px;line-height:12px;color:var(--ink);letter-spacing:.3px}
  .contact span{display:block;white-space:nowrap;text-align:justify;text-align-last:justify}
</style>
</head>
<body>
<main class="canvas">

  <section class="flyer flyer--front" aria-label="Flyer Vorderseite">
    <div class="hero-photo" role="img" aria-label="Foto: Kopierer gibt ein Blatt mit der Erdkugel aus"></div>
    <p class="claim claim--help">Helfen Sie uns,<br>nachhaltig<br>zu wirtschaften …</p>
    <p class="claim claim--planet">… denn<br>unser Planet<br>lässt sich<br>nicht kopieren!</p>
    <p class="brand">brettel Büroservice</p>
    <p class="band">+++ VERMIETUNG NEUWERTIGER GEBRAUCHTGERÄTE +++</p>
  </section>

  <section class="flyer flyer--back" aria-label="Flyer Rückseite">
    <h2 class="headline">FRÜHER ODER SPÄTER WIRD ALLES WEGGEWORFEN</h2>
    <p class="copy copy--intro-a">
      <span>In unserer Konsumgesellschaft wan-</span>
      <span>dern aber auch gebrauchsfertige und</span>
      <span>neuwertige Produkte auf dem Müll.</span>
      <span class="end">Dieses hat fatale Konsequenzen:</span>
    </p>
    <p class="copy copy--intro-b">
      <span>Klimawandel, Artensterben, Wasser-</span>
      <span>mangel. So wie wir wirtschaften, kann</span>
      <span>es nicht weitergehen! Helfen Sie uns,</span>
      <span>Rohstoffe möglichst lange zu nutzen.</span>
    </p>

    <svg class="cycle" width="450" height="450" viewBox="0 0 450 450" aria-hidden="true">
      <g fill="none" stroke-linecap="butt">
        <path d="M92 150 Q76 114 114 104" stroke="var(--teal)" stroke-width="13"/>
        <path d="M92 150 Q86 138 85 126" stroke="var(--teal-dark)" stroke-width="9"/>
        <path d="M352 131 Q396 120 398 160" stroke="var(--teal)" stroke-width="13"/>
        <path d="M352 131 Q362 126 372 125" stroke="var(--teal-dark)" stroke-width="9"/>
        <path d="M325 270 Q320 300 288 290" stroke="var(--teal)" stroke-width="13"/>
        <path d="M325 270 Q324 282 316 292" stroke="var(--teal-dark)" stroke-width="9"/>
        <path d="M128 272 Q88 282 90 242" stroke="var(--teal)" stroke-width="13"/>
        <path d="M128 272 Q118 276 108 276" stroke="var(--teal-dark)" stroke-width="9"/>
      </g>
      <g fill="var(--teal)">
        <polygon points="106,91 132,100 114,119"/>
        <polygon points="386,157 410,157 398,182"/>
        <polygon points="269,266 298,278 280,302"/>
        <polygon points="77,245 103,245 90,220"/>
      </g>
    </svg>
    <div class="device device--copier" role="img" aria-label="Foto: großer Kopierautomat mit Finisher"></div>
    <div class="device device--printer" role="img" aria-label="Foto: kompakter weißer Drucker"></div>

    <span class="step-no step-no--1">1</span>
    <p class="step step--1">Ankauf<br>gebrauchter<br>Leasing-Geräte</p>
    <span class="step-no step-no--2">2</span>
    <p class="step step--2">Aufbereitung<br>in unserer<br>Werkstatt</p>
    <span class="step-no step-no--3">3</span>
    <p class="step step--3">Vermietung dieser<br>neuwertigen<br>Geräte</p>
    <p class="together">Gemeinsam<br>wirtschaften<br>wir nachhaltig</p>

    <h2 class="headline headline--sub">HELFEN SIE MIT …</h2>
    <p class="copy copy--join-a">
      <span>… beim Aufbau einer erfolgreichen</span>
      <span>Nutzungsform, bei der funktions-</span>
      <span>tüchtige Kopierautomaten weiterhin</span>
    </p>
    <p class="copy copy--join-b">
      <span>eingesetzt werden sodass sicher-</span>
      <span>gestellt wird, daß Rohstoffe mög-</span>
      <span>lichst lange genutzt werden, um</span>
      <span>dadurch die Umwelt zu schonen.</span>
    </p>

    <p class="contact">
      <span>brettel Büroservice GmbH, Lindenweg 8, 50321 Brühlstadt</span>
      <span>02271 – 48 20 93, info@brettel-bueroservice.de, www.brettel-bueroservice.de</span>
    </p>

    <p class="band">+++ BITTE BEACHTEN SIE UNSER BEIGEFÜGTES ANGEBOT +++</p>
  </section>

</main>
</body>
</html>
```